Web Design Project for Web Agency

WHAT I NEED:
The design I need (PSD file) is for a microsite designed for employee recruitment for Brennick, a Web agency.
***Design for the 1st Page ONLY : "Manifeste"
OBJECTIVES OF THE WEBSITE:
1. To promote the agency's corporate culture and HR management principles.
2. To get people to apply on available jobs
ELEMENTS OF THE PAGE "MANIFESTE" :
1. Brennick logo (see attached files). Beside the logo must be the word "Carrières" ("Careers" in english)
***The logo is not final and there is NO branding for Brennick yet. That is why there are multiple files. So please feel free to be creative!
2. Main menu : 4 sections
Manifeste | Opportunités | Brenick | Postuler
3. Manifeste :
This page is the home page. It will present 2 main sections :
a. The agency's corporate culture :
- Title of the page is a question : "Do you embrace Brennick's corporate culture?"
- Then, presentation of the 5 corporate values, each with a title and short description
- At the end of the list of values, we want a button that says "Apply now"
b. The agency's HR management principles :
- Title of the page is a question : "Do you see yourself working at Brennick?"
- Then, presentation of the 5 Management principles, each with a title and short description
- At the end of the list of principles, we want a button that says "Apply now"
VISUAL INSPIRATION
To create each section of the "Manifeste" page, we want a design that will fit with the corporate culture:
- Brennick is BOLD
- Brennick is PROUD
- Brennick is PROFESSIONAL
- Brennick is ELEGANT
- Brennick is REFINED
We want something slick and modern. Here are some Website's that we like that can be of inspiration:
- http://www.studio-varnel.com/en/services
- http://quillmorrowlab.com/

```html
<!DOCTYPE html>
<html lang="fr">
<head>
<meta charset="utf-8">
<title>Brennick — Manifeste</title>
<link href="https://fonts.googleapis.com/css2?family=Source+Sans+3:wght@400;600&display=swap" rel="stylesheet">
<style>
  :root {
    --orange: #e8611e;
    --blue: #1e5a94;
    --blue-btn: #1a4fa8;
    --text: #333;
    --muted: #555;
    --panel: #e8e8e8;
    --footer: #e6e5e3;
    --footer-dark: #3d3d3d;
    --white: #fff;
  }
  * { box-sizing: border-box; margin: 0; padding: 0; }
  html, body { width: 962px; height: 1200px; overflow: hidden; }
  body { position: relative; background: var(--white); font-family: "Source Sans 3", sans-serif; color: var(--text); }
  .abs { position: absolute; }

  .site-header { position: absolute; left: 0; top: 0; width: 962px; height: 89px; background: var(--white); }
  .brand { position: absolute; left: 69px; top: 18px; font-size: 36px; font-weight: 600; color: var(--orange); letter-spacing: 0.5px; }
  .main-nav { position: absolute; top: 48px; left: 0; width: 962px; font-size: 17px; color: #333; }
  .main-nav span { position: absolute; white-space: nowrap; }

  .hero { position: absolute; left: 0; top: 89px; width: 962px; height: 375px;
    background: linear-gradient(100deg, #c9d5e6 0%, #a9bbd4 22%, #e4eaf2 42%, #3c4f72 58%, #e9edf3 70%, #1f2c4a 84%, #d6dde7 100%); }
  .hero-caption { position: absolute; left: 69px; top: 191px; width: 336px; height: 102px; background: rgba(60,64,72,0.82); color: var(--white); padding: 14px 14px; }
  .hero-caption h2 { font-size: 21px; font-weight: 600; margin-bottom: 6px; }
  .hero-caption p { font-size: 13px; line-height: 20px; }
  .slider-dots { position: absolute; left: 840px; top: 352px; display: flex; gap: 3px; }
  .slider-dots i { width: 11px; height: 11px; border-radius: 50%; background: #ddd; border: 1px solid #aaa; }
  .slider-dots i:first-child { background: #777; }

  .welcome { position: absolute; left: 0; top: 486px; width: 962px; text-align: center; }
  .welcome h1 { font-size: 20px; font-weight: 600; color: #333; }
  .welcome p { font-size: 13px; line-height: 23px; color: var(--muted); margin-top: 10px; }
  .btn-dark { display: inline-block; background: linear-gradient(#3a3a3a, #111); color: var(--white); font-size: 12px; border-radius: 3px; text-transform: uppercase; box-shadow: 0 2px 3px rgba(0,0,0,0.35); }
  .welcome .btn-dark { margin-top: 10px; width: 99px; height: 30px; line-height: 30px; }
  .divider { position: absolute; left: 90px; top: 626px; width: 780px; height: 8px; background: radial-gradient(ellipse at center top, rgba(0,0,0,0.10), transparent 70%); }

  .col { position: absolute; top: 668px; width: 394px; }
  .col h3 { font-size: 20px; font-weight: 400; color: var(--orange); height: 37px; }
  .card { border: 1px solid #ddd; border-top: 5px solid var(--orange); height: 250px; background: var(--white); box-shadow: 0 6px 6px -6px rgba(0,0,0,0.2); }
  .card-head { background: var(--panel); height: 50px; line-height: 50px; padding-left: 12px; font-size: 15px; color: var(--blue); text-transform: uppercase; }
  .card ul { list-style: none; padding: 13px 12px 0; }
  .card li { font-size: 12.5px; height: 29px; display: flex; align-items: center; gap: 9px; color: #333; }
  .card .btn-dark { margin: 3px 0 0 12px; width: 86px; height: 22px; line-height: 22px; text-align: center; font-size: 11px; border-radius: 2px; }

  .site-footer { position: absolute; left: 0; top: 994px; width: 962px; height: 156px; background: var(--footer); font-size: 11px; color: #333; }
  .foot-col { position: absolute; top: 13px; }
  .foot-col li { list-style: none; height: 23px; }
  .foot-col .head { text-transform: uppercase; }
  .foot-title { font-size: 13px; }
  .field { position: absolute; width: 131px; height: 25px; background: var(--white); font-size: 11px; color: #777; padding: 7px 8px; }
  .submit { position: absolute; left: 636px; top: 122px; width: 59px; height: 21px; background: var(--blue-btn); color: var(--white); font-size: 11px; text-align: center; line-height: 21px; }
  .social { position: absolute; left: 759px; display: flex; align-items: center; gap: 12px; font-size: 12.5px; }
  .social i { width: 26px; height: 26px; border-radius: 4px; display: block; }
  .bottom-bar { position: absolute; left: 0; top: 1150px; width: 962px; height: 50px; background: var(--footer-dark); color: var(--white); font-size: 11px; padding: 20px 69px; }
</style>
</head>
<body>
  <header class="site-header">
    <div class="brand">Brennick</div>
    <nav class="main-nav">
      <span style="left:485px">Manifeste</span>
      <span style="left:595px">Opportunités</span>
      <span style="left:734px">Brenick</span>
      <span style="left:832px">Postuler</span>
    </nav>
  </header>

  <section class="hero" role="img" aria-label="Photo of a business team in suits reviewing documents at a desk in a glass office">
    <div class="hero-caption">
      <h2>Amet dolor sit tation ullamcorper</h2>
      <p>Donec id ante magna. Nullam sollicitudin, ipsum vel hendrerit aliquam, nisi sapien pellentesque odio.</p>
    </div>
    <div class="slider-dots"><i></i><i></i><i></i><i></i></div>
  </section>

  <section class="welcome">
    <h1>Welcome to our Website</h1>
    <p>Claritas est etiam processus dynamicus, qui sequitur mutationem consuetudium lectorum. Mirum est notare quam littera gothica,<br>quam nunc putamus parum claram, anteposuerit litterarum formas humanitatis per seacula quarta decima et quinta decima.</p>
    <span class="btn-dark">Read More</span>
  </section>
  <div class="divider"></div>

  <section class="col" style="left:69px">
    <h3>Corporate culture</h3>
    <div class="card">
      <div class="card-head">Do you embrace Brennick's corporate culture?</div>
      <ul>
        <li><svg width="13" height="13" viewBox="0 0 13 13"><rect x="1" y="2" width="9" height="9" fill="none" stroke="#555" stroke-width="1.2" rx="2"/><path d="M3 6l2.5 2.5L12 1.5" fill="none" stroke="#555" stroke-width="1.6"/></svg>Sed ut perspiciatis unde omnis iste natus error sit votum.</li>
        <li><svg width="13" height="13" viewBox="0 0 13 13"><rect x="1" y="2" width="9" height="9" fill="none" stroke="#555" stroke-width="1.2" rx="2"/><path d="M3 6l2.5 2.5L12 1.5" fill="none" stroke="#555" stroke-width="1.6"/></svg>Eaque ipsa quae ab illo inventore veritatis et quasi.</li>
        <li><svg width="13" height="13" viewBox="0 0 13 13"><rect x="1" y="2" width="9" height="9" fill="none" stroke="#555" stroke-width="1.2" rx="2"/><path d="M3 6l2.5 2.5L12 1.5" fill="none" stroke="#555" stroke-width="1.6"/></svg>Lorem ipsum dolor sit amet, consectetur adipisicing elit.</li>
        <li><svg width="13" height="13" viewBox="0 0 13 13"><rect x="1" y="2" width="9" height="9" fill="none" stroke="#555" stroke-width="1.2" rx="2"/><path d="M3 6l2.5 2.5L12 1.5" fill="none" stroke="#555" stroke-width="1.6"/></svg>Sed do eiusmod tempor incididunt ut labore et dolore aliqua.</li>
        <li><svg width="13" height="13" viewBox="0 0 13 13"><rect x="1" y="2" width="9" height="9" fill="none" stroke="#555" stroke-width="1.2" rx="2"/><path d="M3 6l2.5 2.5L12 1.5" fill="none" stroke="#555" stroke-width="1.6"/></svg>Ut enim ad minim veniam, quis nostrud exercitation.</li>
      </ul>
      <span class="btn-dark">Apply Now</span>
    </div>
  </section>

  <section class="col" style="left:499px">
    <h3>HR management principles</h3>
    <div class="card">
      <div class="card-head">Do you see yourself working at Brennick?</div>
      <ul>
        <li><svg width="13" height="13" viewBox="0 0 13 13"><rect x="1" y="2" width="9" height="9" fill="none" stroke="#555" stroke-width="1.2" rx="2"/><path d="M3 6l2.5 2.5L12 1.5" fill="none" stroke="#555" stroke-width="1.6"/></svg>Sed ut perspiciatis unde omnis iste natus error sit votum.</li>
        <li><svg width="13" height="13" viewBox="0 0 13 13"><rect x="1" y="2" width="9" height="9" fill="none" stroke="#555" stroke-width="1.2" rx="2"/><path d="M3 6l2.5 2.5L12 1.5" fill="none" stroke="#555" stroke-width="1.6"/></svg>Eaque ipsa quae ab illo inventore veritatis et quasi.</li>
        <li><svg width="13" height="13" viewBox="0 0 13 13"><rect x="1" y="2" width="9" height="9" fill="none" stroke="#555" stroke-width="1.2" rx="2"/><path d="M3 6l2.5 2.5L12 1.5" fill="none" stroke="#555" stroke-width="1.6"/></svg>Lorem ipsum dolor sit amet, consectetur adipisicing elit.</li>
        <li><svg width="13" height="13" viewBox="0 0 13 13"><rect x="1" y="2" width="9" height="9" fill="none" stroke="#555" stroke-width="1.2" rx="2"/><path d="M3 6l2.5 2.5L12 1.5" fill="none" stroke="#555" stroke-width="1.6"/></svg>Sed do eiusmod tempor incididunt ut labore et dolore aliqua.</li>
        <li><svg width="13" height="13" viewBox="0 0 13 13"><rect x="1" y="2" width="9" height="9" fill="none" stroke="#555" stroke-width="1.2" rx="2"/><path d="M3 6l2.5 2.5L12 1.5" fill="none" stroke="#555" stroke-width="1.6"/></svg>Ut enim ad minim veniam, quis nostrud exercitation.</li>
      </ul>
      <span class="btn-dark">Apply Now</span>
    </div>
  </section>

  <footer class="site-footer">
    <ul class="foot-col" style="left:72px"><li class="head">Company</li><li>About</li><li>Contact</li><li>Legals &amp; Privacy</li><li>Niptaiades Keuytaser</li><li>Nemosera Lasecaerat</li></ul>
    <ul class="foot-col" style="left:250px"><li class="head">More</li><li>How it Works</li><li>FAQ</li><li>Media Centre</li><li>Suggest a Business</li><li>Blog</li></ul>
    <ul class="foot-col" style="left:414px"><li class="head">Offer a Deal</li><li>Media Owners</li><li>Marketing Providers</li><li>Nemosera Lasecaerat</li><li>Binsequuntur</li><li>Dolar ipsum</li></ul>
    <div class="abs foot-title" style="left:564px;top:11px">Newsletter Signup</div>
    <div class="field" style="left:564px;top:47px">Name</div>
    <div class="field" style="left:564px;top:83px">Email Id</div>
    <div class="submit">SUBMIT</div>
    <div class="abs foot-title" style="left:759px;top:11px">Connect with us</div>
    <div class="social" style="top:43px"><i style="background:#3b5a9a"></i>Folkbook</div>
    <div class="social" style="top:75px"><i style="background:#c8232c"></i>PinBoardly</div>
    <div class="social" style="top:109px"><i style="background:#2fa9e0"></i>Chirper</div>
  </footer>
  <div class="bottom-bar">Copyrights 2013. All Rights Reserved.</div>
</body>
</html>
```